BRIGHTWAVE DENTAL *

please see attached.

Target Market(s)

Adults 18-60

Contact Information for Business Card

Website: brightwavedentalqz.com
Phone number 555 304 7726 email: brightwavedentalqz@mailvex.com
Address:417 S. Kellim rd
Suite#24, TX70000
Dr. Elias Varno, DDS

Font styles to use
Sans Serif

Requirements
Must have
• Logo, phone number website, doctor,
• 's name

```html
<!DOCTYPE html>
<html lang="en">
<head>
<meta charset="utf-8">
<title>Brightwave Dental – Business Card</title>
<link href="https://fonts.googleapis.com/css2?family=Open+Sans:wght@400;700&display=swap" rel="stylesheet">
<style>
  :root {
    --stage: #ecebea;
    --card-white: #ffffff;
    --panel-grey: #524d4d;
    --accent-teal: #138ea3;
    --text-light: #ffffff;
    --brand-ink: #4a4546;
    --ring-grey: #5a5556;
  }
  * { margin: 0; padding: 0; box-sizing: border-box; }
  html, body {
    width: 1200px;
    height: 900px;
    overflow: hidden;
    background: var(--stage);
    font-family: "Open Sans", Arial, sans-serif;
  }
  .business-card {
    position: absolute;
    left: 160px;
    top: 178px;
    width: 880px;
    height: 544px;
    background: var(--card-white);
    overflow: hidden;
    box-shadow: 0 10px 30px rgba(0,0,0,0.12);
  }
  .card-panel {
    position: absolute;
    inset: 0;
    width: 880px;
    height: 544px;
  }
  .doctor-name {
    position: absolute;
    left: 53px;
    top: 150px;
    color: var(--text-light);
    font-weight: 700;
    font-size: 33px;
    letter-spacing: 0.2px;
  }
  .doctor-name .credential {
    font-weight: 400;
    font-size: 25px;
  }
  .contact-list {
    position: absolute;
    left: 53px;
    top: 302px;
    list-style: none;
    color: var(--text-light);
    font-size: 26px;
    line-height: 41px;
  }
  .contact-list li {
    display: flex;
    align-items: center;
    gap: 10px;
  }
  .contact-icon { width: 26px; height: 26px; flex: none; }
  .brand {
    position: absolute;
    left: 478px;
    width: 380px;
    top: 278px;
    text-align: center;
  }
  .brand-circle {
    display: block;
    margin: 0 auto 42px;
    width: 124px;
    height: 124px;
    border: 3px solid var(--ring-grey);
    border-radius: 50%;
  }
  .brand-name {
    color: var(--brand-ink);
    font-weight: 400;
    font-size: 30px;
    letter-spacing: 1.5px;
    white-space: nowrap;
  }
</style>
</head>
<body>
  <div class="business-card">
    <svg class="card-panel" viewBox="0 0 880 544" aria-hidden="true">
      <path d="M0 0 H346 Q676 272 346 544 H0 Z" fill="var(--accent-teal)"/>
      <path d="M0 0 H332 Q654 272 332 544 H0 Z" fill="var(--panel-grey)"/>
    </svg>

    <h1 class="doctor-name">DR. ELIAS VARNO<span class="credential">, DDS</span></h1>

    <ul class="contact-list">
      <li>
        <svg class="contact-icon" viewBox="0 0 24 24" aria-hidden="true">
          <path d="M3 9c0-3 4-5 9-5s9 2 9 5v2h-5V9c-1-1-7-1-8 0v2H3z" fill="#fff"/>
          <path d="M7 12h10l3 8H4z" fill="#fff"/>
          <circle cx="12" cy="16" r="2" fill="var(--panel-grey)"/>
        </svg>
        <span>555 304 7726</span>
      </li>
      <li>
        <svg class="contact-icon" viewBox="0 0 24 24" aria-hidden="true">
          <circle cx="12" cy="12" r="10" fill="#fff"/>
          <path d="M7 7c2 0 3 1 3 3s-2 2-2 4-2 1-3-1c-1-2 0-6 2-6zM14 13c2 0 3 2 2 4s-3 3-4 2 0-6 2-6z" fill="var(--panel-grey)"/>
        </svg>
        <span>www.brightwavedentalqz.com</span>
      </li>
    </ul>

    <div class="brand">
      <span class="brand-circle" aria-hidden="true"></span>
      <div class="brand-name">BRIGHTWAVE DENTAL</div>
    </div>
  </div>
</body>
</html>
```